Dampfbadtechnik und Ausstattung Produktübersicht 2016/2017
lumavo suchte ein neues Design in der Kategorie Broschüre und hat ein Projekt auf entwurfmarkt.de gestartet.
Zielgruppe
Wir verkaufen die Technik sowie generell die Austattung für Dampfbäder. Sanitärbetriebe, Private Kunden die selbst ein Dampfbad bauen, Fliesenfachbetriebe, Wellnesscenter..
Aufgabenstellung
Alles möglich (Format, Design,..). Es handelt sich um eine Produktübersicht unserer Produkte. Unsere Kunden sind Sanitärbetriebe, Private Kunden die selbst ein Dampfbad bauen, Fliesenfachbetriebe, Wellnesscenter..
Fotos und Texte die Sie für den Folder Verwenden können finden Sie unter:
www.nebelraumwerk.com bzw. www.hitzequelle-vorta.at/de/Referenzen.html
Ich würde gerne Broschüren drucken und den Kunden zusenden.

```html
<!DOCTYPE html>
<html lang="de">
<head>
<meta charset="utf-8">
<title>Übersicht – Produktübersicht</title>
<link href="https://fonts.googleapis.com/css2?family=Quicksand:wght@400;500&family=Open+Sans:wght@400&display=swap" rel="stylesheet">
<style>
  :root {
    --navy: #0b3b7a;
    --cyan: #00b5e6;
    --white: #ffffff;
    --steam-light: #d9d9d6;
    --steam-mid: #c4c3bd;
    --tile: #a9a89e;
  }
  * { margin: 0; padding: 0; box-sizing: border-box; }
  html, body { width: 1200px; height: 423px; overflow: hidden; background: var(--white); }
  .spread { position: relative; width: 1200px; height: 423px; background: var(--white); font-family: "Quicksand", sans-serif; color: var(--navy); }

  .page-title { position: absolute; left: 85px; top: 54px; font-size: 20px; font-weight: 400; letter-spacing: 0.3px; }
  .title-rule { position: absolute; left: 85px; top: 79px; width: 1115px; height: 2px; background: var(--cyan); }

  .toc { position: absolute; left: 85px; top: 113px; width: 185px; list-style: none; }
  .toc-item { display: flex; align-items: baseline; height: 20.2px; font-size: 11px; font-weight: 500; letter-spacing: 0.2px; }
  .toc-label { white-space: nowrap; }
  .toc-dots { flex: 1; margin: 0 5px; border-bottom: 1px dotted var(--navy); transform: translateY(-3px); }
  .toc-page { width: 15px; text-align: right; }

  .intro-panel { position: absolute; left: 343px; top: 118px; width: 183px; height: 305px; background: var(--cyan); }
  .intro-label { position: absolute; left: 7px; top: 9px; font-family: "Open Sans", sans-serif; font-size: 11px; color: var(--white); }

  .hero-image { position: absolute; left: 599px; top: 80px; width: 601px; height: 196px; border: 1.5px solid var(--cyan); border-right: none;
    background: linear-gradient(90deg, var(--tile) 0%, var(--steam-mid) 12%, var(--steam-light) 40%, var(--steam-light) 75%, var(--steam-mid) 92%, var(--tile) 100%); }

  .section-title { position: absolute; right: 86px; top: 296px; font-size: 17.5px; font-weight: 500; letter-spacing: 0.3px; }
  .section-rule { position: absolute; left: 600px; top: 319px; width: 514px; height: 2px; background: var(--cyan); }

  .page-number { position: absolute; left: 1161px; top: 383px; font-family: "Open Sans", sans-serif; font-size: 10px; color: var(--cyan); }
</style>
</head>
<body>
<main class="spread">
  <h1 class="page-title">Übersicht</h1>
  <div class="title-rule"></div>

  <ol class="toc">
    <li class="toc-item"><span class="toc-label">Dampfgeneratoren</span><span class="toc-dots"></span><span class="toc-page">3</span></li>
    <li class="toc-item"><span class="toc-label">Ausstattung</span><span class="toc-dots"></span><span class="toc-page">11</span></li>
    <li class="toc-item"><span class="toc-label">LED Beleuchtung</span><span class="toc-dots"></span><span class="toc-page">12</span></li>
    <li class="toc-item"><span class="toc-label">Duftstoffpumpe „DuoFlora“</span><span class="toc-dots"></span><span class="toc-page">13</span></li>
    <li class="toc-item"><span class="toc-label">Dampfleitung</span><span class="toc-dots"></span><span class="toc-page">14</span></li>
    <li class="toc-item"><span class="toc-label">Dampfbadlautsprecher</span><span class="toc-dots"></span><span class="toc-page">15</span></li>
    <li class="toc-item"><span class="toc-label">Salzsolevernebelung</span><span class="toc-dots"></span><span class="toc-page">16</span></li>
    <li class="toc-item"><span class="toc-label">Dampfbadtür</span><span class="toc-dots"></span><span class="toc-page">18</span></li>
    <li class="toc-item"><span class="toc-label">Dampfsitzbank</span><span class="toc-dots"></span><span class="toc-page">20</span></li>
    <li class="toc-item"><span class="toc-label">Heizmatte</span><span class="toc-dots"></span><span class="toc-page">22</span></li>
    <li class="toc-item"><span class="toc-label">Impressionen</span><span class="toc-dots"></span><span class="toc-page">25</span></li>
  </ol>

  <section class="intro-panel">
    <p class="intro-label">Einleitung</p>
  </section>

  <div class="hero-image" role="img" aria-label="Person in einem Handtuch entspannt sich in einem dampfgefüllten, mosaikgefliesten Dampfbad"></div>

  <h2 class="section-title">Dampfgeneratoren</h2>
  <div class="section-rule"></div>

  <span class="page-number">3</span>
</main>
</body>
</html>
```